Varemo Group Business Card Design

The CEO is looking for a new trendy look for his business card.
You can stay with current branding or come up with something new/creative. It can be 3D, including Medical Office buildings. You can use our logo in a variety of colors. Please include name, title, company name, company website, email address, cell number

Target Market(s)

Real Estate Development and Construction

Industry/Entity Type

Health care real estate

Contact Information for Business Card

Rohesh Kumbar, CEO M-727.418.9062 E-roheshkumbar@varemo.com Address:4100 Lindell Ave, Tampa, FL 33611 www.varemo.com

Font styles to use
Other font styles liked:
• Be creative

Requirements
Must have
• Creative, trendy look
Nice to have
• Please go to our website to get a feel- www. varemo.com
Should not have
• small fonts

```html
<!DOCTYPE html>
<html lang="en">
<head>
<meta charset="UTF-8">
<title>Varemo Group Business Card</title>
<link href="https://fonts.googleapis.com/css2?family=Archivo:wght@400;500;700;800;900&display=swap" rel="stylesheet">
<style>
  :root {
    --red: #d8141c;
    --ink: #111111;
    --paper: #f4f4f3;
    --bg: #e9e9e9;
    --steel-dark: #3a3d42;
    --steel-light: #b9bdc2;
    --sky: #7fb4d1;
    --sky-light: #cfe3ee;
  }
  * { box-sizing: border-box; margin: 0; padding: 0; }
  html, body {
    width: 1200px; height: 1027px; overflow: hidden;
    background: var(--bg);
    font-family: "Archivo", Arial, sans-serif;
  }
  .canvas {
    width: 1200px; height: 1027px;
    display: flex; flex-direction: column; align-items: center; justify-content: center;
    gap: 30px;
  }
  .card {
    position: relative;
    width: 840px; height: 468px;
    background: var(--paper);
    overflow: hidden;
    box-shadow: 0 10px 28px rgba(0,0,0,0.14);
  }

  /* Front */
  .front-corner {
    position: absolute; left: 0; top: 0;
    width: 0; height: 0;
    border-top: 34px solid var(--red);
    border-right: 34px solid transparent;
  }
  .front-frame {
    position: absolute; left: 70px; top: 70px; width: 560px; height: 330px;
    border: 3px solid var(--red);
  }
  .front-photo {
    position: absolute; left: 470px; top: 110px; width: 370px; height: 358px;
    background: linear-gradient(160deg, var(--steel-light) 0%, #7c8187 45%, var(--steel-dark) 100%);
    clip-path: polygon(14% 0, 100% 0, 100% 100%, 0 100%, 0 30%);
  }
  .brand-name {
    position: absolute; left: 112px; top: 190px;
    font-size: 84px; font-weight: 900; color: var(--red);
    letter-spacing: -2px; line-height: 1;
  }
  .web-tag {
    position: absolute; left: 470px; top: 352px;
    background: var(--red); color: #fff;
    font-size: 20px; font-weight: 500;
    padding: 6px 16px;
  }

  /* Back */
  .back-photo {
    position: absolute; right: 0; top: 0; width: 320px; height: 468px;
    background: linear-gradient(180deg, var(--sky) 0%, var(--sky-light) 55%, #e6eef2 80%, #9fb08f 100%);
  }
  .name-bar {
    position: absolute; left: 58px; top: 70px; width: 26px; height: 128px;
    background: var(--red);
  }
  .name-bar svg { position: absolute; left: 5px; top: 70px; }
  .holder-name {
    position: absolute; left: 110px; top: 88px;
    font-size: 46px; font-weight: 800; color: var(--ink); letter-spacing: -0.5px;
    white-space: nowrap;
  }
  .holder-title {
    position: absolute; left: 112px; top: 150px;
    font-size: 20px; font-weight: 400; color: var(--red);
  }
  .contact-list {
    position: absolute; left: 84px; top: 216px;
    list-style: none;
  }
  .contact-list li {
    display: flex; align-items: center; gap: 22px;
    height: 50px;
    font-size: 23px; color: var(--ink);
    white-space: nowrap;
  }
  .contact-list svg { width: 22px; height: 22px; flex: none; }
  .foot-block {
    position: absolute; left: 104px; bottom: 0; width: 28px; height: 38px;
    background: var(--red);
  }
</style>
</head>
<body>
<main class="canvas">

  <section class="card card-front">
    <div class="front-photo" role="img" aria-label="Photo of a curved glass and steel office building"></div>
    <div class="front-corner"></div>
    <div class="front-frame"></div>
    <div class="brand-name">Varemo</div>
    <div class="web-tag">www.varemo.com</div>
  </section>

  <section class="card card-back">
    <div class="back-photo" role="img" aria-label="Illustration of a modern hospital building under a blue sky"></div>
    <div class="name-bar">
      <svg width="16" height="18" viewBox="0 0 16 18"><circle cx="8" cy="5" r="4" fill="#fff"/><path d="M0 18 C0 11 16 11 16 18 Z" fill="#fff"/></svg>
    </div>
    <h1 class="holder-name">Rohesh Kumbar</h1>
    <p class="holder-title">Company CEO</p>
    <ul class="contact-list">
      <li><svg viewBox="0 0 24 24"><path d="M6.6 10.8a15 15 0 0 0 6.6 6.6l2.2-2.2a1 1 0 0 1 1-.25 11.4 11.4 0 0 0 3.6.57 1 1 0 0 1 1 1V20a1 1 0 0 1-1 1A17 17 0 0 1 3 4a1 1 0 0 1 1-1h3.5a1 1 0 0 1 1 1c0 1.25.2 2.45.57 3.57a1 1 0 0 1-.25 1z" fill="var(--red)"/></svg>727.418.9062</li>
      <li><svg viewBox="0 0 24 24"><rect x="2" y="5" width="20" height="14" rx="1.5" fill="var(--red)"/><polyline points="3,6 12,13 21,6" fill="none" stroke="#fff" stroke-width="1.8"/></svg>roheshkumbar@varemo.com</li>
      <li><svg viewBox="0 0 24 24"><path d="M12 2a7 7 0 0 0-7 7c0 5 7 13 7 13s7-8 7-13a7 7 0 0 0-7-7z" fill="var(--red)"/><circle cx="12" cy="9" r="2.6" fill="#fff"/></svg>4100 Lindell Ave, Tampa, FL 33611</li>
      <li><svg viewBox="0 0 24 24"><circle cx="12" cy="12" r="10" fill="var(--red)"/><g fill="none" stroke="#fff" stroke-width="1.4"><ellipse cx="12" cy="12" rx="4" ry="10"/><line x1="2" y1="12" x2="22" y2="12"/><line x1="4" y1="7" x2="20" y2="7"/><line x1="4" y1="17" x2="20" y2="17"/></g></svg>www.varemo.com</li>
    </ul>
    <div class="foot-block"></div>
  </section>

</main>
</body>
</html>
```